Corporate Material
Powerpoint/Word-Manual Templates
#21 can you remove the globe image and use a more modern theme and incorporate more cloud and technology type images.
#17 can you make the logo in the bottom left corners a little smaller I do not want the logo to over power the presentation. Also i would like to see the manual.
Also can you add a few cloud images to your presentation cover.
#16 please show me a example of a page with the subject header and body
Contest is extended for 2 more days.
-Ruth
I am interested in have a custom powerpoint template design for my company.
We are a technology company looking for a template that will allow us to introduce ourselves to prospective customers.
Innovation, Cloud Computing and Cloud Lifecycle Management.
Out target customer is the Public Sector (Government Customers)
The microsoft word template is a word template that will be used to developed corporate manuals so looking for a clean corporate cover page design and formatted header a footer.
1. Powerpoint Presentation
The presentation Title Master should have images of innovative technology to include cloud, government, and management consulting images.
I would like to see on the slide pages a header area that has technology images in the right corner so a title can be added to the slide.
The footer of the slide should have a subdued corporate logo in the bottom left corner.
I hope this helps.
This will be used as a corporate capabilities statement presentation
I would need more detailed scheme of the structure of Word Teplate. I've made one draft, but it could be way better if I know what exactly is my job.
Kindly give the link of your website,,
Dlpn-us site info
Designers I have not had any input on this effort.....
Innovative, technology focused images but a clean corporate look.
Ok, designers I am looking for presentations that will provide customers with a mature innovative technology company. So I am looking for some clean corporate images to be part of the templates. please review company website for additional details if required.
Looking for Executive Briefing powerpoint template and microsoft word template is what i am looking for.

```html
<!DOCTYPE html>
<html lang="en">
<head>
<meta charset="utf-8">
<title>Can IT be complex? – DLPN manual page</title>
<link rel="stylesheet" href="https://fonts.googleapis.com/css2?family=Arimo:wght@400;700&display=swap">
<style>
  :root {
    --canvas-bg: #e8edf1;
    --page-bg: #cfe1e7;
    --title-blue: #1b3f73;
    --brand-teal: #2a97c6;
    --box-bg: #ffffff;
    --box-border: #2b2f36;
    --body-grey: #6f7479;
    --sky-deep: #2d6fb8;
    --sky-mid: #6ea5da;
    --sky-light: #dfeaf4;
  }
  * { box-sizing: border-box; margin: 0; padding: 0; }
  html, body {
    width: 1200px;
    height: 901px;
    overflow: hidden;
    background: var(--canvas-bg);
    font-family: "Arimo", Arial, sans-serif;
  }
  .manual-page {
    position: absolute;
    left: 297px;
    top: 20px;
    width: 605px;
    height: 860px;
    background: var(--page-bg);
  }
  .page-title {
    position: absolute;
    left: 72px;
    top: 76px;
    font-size: 25px;
    font-weight: 700;
    color: var(--title-blue);
  }
  .brand-name {
    position: absolute;
    left: 372px;
    top: 58px;
    font-size: 42px;
    font-weight: 700;
    letter-spacing: 2px;
    color: var(--brand-teal);
  }
  .text-box {
    position: absolute;
    left: 72px;
    width: 473px;
    height: 180px;
    background: var(--box-bg);
    border: 1.5px solid var(--box-border);
    padding: 10px 12px;
  }
  .text-box--upper { top: 136px; }
  .text-box--lower { top: 598px; }
  .text-box p {
    font-size: 9.6px;
    line-height: 1.42;
    color: var(--body-grey);
    margin-bottom: 10px;
  }
  .feature-photo {
    position: absolute;
    left: 131px;
    top: 335px;
    width: 362px;
    height: 234px;
    background:
      radial-gradient(ellipse at 30% 70%, var(--sky-light) 0%, rgba(223,234,244,0) 45%),
      radial-gradient(ellipse at 80% 25%, rgba(255,255,255,0.7) 0%, rgba(255,255,255,0) 40%),
      linear-gradient(160deg, var(--sky-deep) 0%, var(--sky-mid) 60%, var(--sky-light) 100%);
  }
</style>
</head>
<body>
  <main class="manual-page">
    <h1 class="page-title">Can IT be complex?</h1>
    <div class="brand-name">DLPN</div>

    <section class="text-box text-box--upper">
      <p>Integer erat ipsum, adipiscing non luctus nec, auctor quis quam. Suspendisse potenti. Cras in tempor augue. Maecenas augue dui, semper vel congue vel, porttitor ac urna. Nulla volutpat felis sed neque pellentesque mollis. Etiam vitae elit tellus, sed tristique risus. Maecenas metus purus, vestibulum at justo nisi, pellentesque consectetur.</p>
      <p>Praesent leo magna, ultrices sed fermentum eu, dapibus ac turpis. Aliquam ac ipsum aliquet risus luctus tempus eu eget leo. Nullam a malesuada est luctus tincidunt. Duis ac nulla nec elit molestie luctus sit amet quis. Donec vitae neque imperdiet sapien dictum pretium.</p>
    </section>

    <div class="feature-photo" role="img" aria-label="Photo of street signposts reading global, summit, business and success against a bright cloudy blue sky"></div>

    <section class="text-box text-box--lower">
      <p>Integer erat ipsum, adipiscing non luctus nec, auctor quis quam. Suspendisse potenti. Cras in tempor augue. Maecenas augue dui, semper vel congue vel, porttitor ac urna. Nulla volutpat felis sed neque pellentesque mollis. Etiam vitae elit tellus, sed tristique risus. Maecenas metus purus, vestibulum at justo nisi, pellentesque consectetur.</p>
      <p>Praesent leo magna, ultrices sed fermentum eu, dapibus ac turpis. Aliquam ac ipsum aliquet risus luctus tempus eu eget leo. Nullam a malesuada est luctus tincidunt. Duis ac nulla nec elit molestie luctus sit amet quis. Donec vitae neque imperdiet sapien dictum pretium.</p>
    </section>
  </main>
</body>
</html>
```